TovaLamishpacha - Israeli Mental Health Website

We are developing an Israeli website for mental health. The website will be both in English and in Hebrew. We have a logo and would like a website design based on the logo and the logos colors (attached).

Attached is a doc that contains the website requirements.

We would like to have an icon for each of the sidebar categories, an image for each of the pages (including each of the sidebar category pages).

Target Market(s)

Adults 18-80

Industry/Entity Type

Mental Health

Number of Pages Required

5+ page

Font styles to use
Sans Serif

Colors

Designer to choose colors to be used in the design.

```html
<!DOCTYPE html>
<html lang="en">
<head>
<meta charset="utf-8">
<title>TovaLamishpacha – Mental Health</title>
<link href="https://fonts.googleapis.com/css2?family=Roboto:wght@400;500;700&display=swap" rel="stylesheet">
<style>
:root{
  --blue:#1f72bd;
  --nav-blue:#2a6fb0;
  --green:#4cae45;
  --logo-green:#5aa94a;
  --ink:#111;
  --white:#fff;
  --side-light:#aecbe6;
  --side-dark:#2d4b6c;
}
*{box-sizing:border-box;margin:0;padding:0}
html,body{width:1200px;height:957px;overflow:hidden;background:var(--white);font-family:'Roboto',sans-serif}
.page{position:relative;width:1200px;height:957px}
.lang{position:absolute;left:954px;top:24px;width:144px;height:27px;border:1px solid var(--blue);border-radius:6px;display:flex;overflow:hidden;font-size:14px}
.lang span{flex:1;display:flex;align-items:center;justify-content:center;color:#222}
.lang .active{background:var(--blue);color:var(--white)}
.brand{position:absolute;left:96px;top:60px;display:flex;align-items:center;gap:8px}
.brand-dot{width:44px;height:44px;border-radius:50%;background:var(--blue)}
.brand-name{font-size:19px;font-weight:700;color:var(--logo-green)}
.nav{position:absolute;left:358px;top:74px;display:flex;gap:26.5px;font-size:16px;font-weight:500;color:var(--nav-blue)}
.phone-pill{position:absolute;display:flex;align-items:center;border:2px solid var(--green);border-radius:8px}
.phone-pill .ico{position:absolute;border-radius:50%;background:var(--green);display:flex;align-items:center;justify-content:center}
.head-phone{left:944px;top:68px;width:154px;height:30px;padding-left:40px;font-size:14px;background:var(--white);color:var(--ink)}
.head-phone .ico{left:-2px;top:-5px;width:36px;height:36px}
.hero{position:absolute;left:351px;top:130px;width:849px;height:727px;
  background:
   linear-gradient(180deg,#fff 0%,rgba(255,255,255,.6) 3%,rgba(255,255,255,0) 8%),
   linear-gradient(180deg,rgba(0,0,0,0) 45%,rgba(0,0,0,.85) 72%,#000 82%),
   radial-gradient(ellipse 30% 28% at 55% 42%,#c99a7c 0%,#a8775a 45%,rgba(120,85,65,0) 100%),
   radial-gradient(ellipse 45% 30% at 82% 18%,#d9b4a2 0%,rgba(200,160,140,0) 100%),
   linear-gradient(160deg,#ece3df 0%,#9a8f8c 30%,#4c4a4c 55%,#1c1a1a 75%)}
.hero-text{position:absolute;left:390px;top:499px;width:565px;font-size:13.5px;line-height:16px;font-weight:500;color:var(--white)}
.hero-phone{left:390px;top:614px;width:261px;height:50px;padding-left:70px;font-size:22px;color:var(--white);border-width:3px}
.hero-phone .ico{left:-3px;top:-7px;width:60px;height:60px}
.sidebar{position:absolute;left:0;top:130px;width:351px;height:806px;border-radius:0 8px 8px 0;
  background:linear-gradient(180deg,var(--side-light) 0%,#9fb9d3 12%,#6b8cae 35%,var(--side-dark) 60%,#3f628a 85%,var(--side-light) 92%)}
.cat{position:absolute;left:90px;width:250px;height:62px;border-bottom:1px solid rgba(255,255,255,.55);display:flex;align-items:center}
.cat:last-child{border-bottom:none}
.cat-ico{width:44px;height:44px;margin-left:14px;flex:none;display:block}
.cat-name{margin-left:10px;font-size:12.5px;font-weight:700;color:var(--ink);line-height:14px;padding-top:2px}
.card{position:absolute;top:726px;width:205px;height:231px;border-radius:8px 8px 0 0;overflow:hidden;background:var(--blue)}
.card-img{height:142px}
.card-body{padding:14px 21px;color:var(--white)}
.card-title{font-size:24px;font-weight:700;line-height:26px}
.card-text{font-size:12.5px;margin-top:8px}
</style>
</head>
<body>
<div class="page">
  <div class="lang"><span class="active">English</span><span>עברית</span></div>
  <div class="brand"><div class="brand-dot"></div><span class="brand-name">TovaLamishpacha</span></div>
  <nav class="nav"><span>Therapists</span><span>Organizations</span><span>Videos</span><span>Contact</span><span>About</span><span>Donate</span></nav>
  <div class="phone-pill head-phone"><span class="ico"><svg width="18" height="18" viewBox="0 0 24 24"><path fill="#fff" d="M6.6 10.8c1.4 2.8 3.8 5.1 6.6 6.6l2.2-2.2c.3-.3.7-.4 1-.2 1.1.4 2.3.6 3.6.6.6 0 1 .4 1 1V20c0 .6-.4 1-1 1C10.6 21 3 13.4 3 4c0-.6.4-1 1-1h3.5c.6 0 1 .4 1 1 0 1.3.2 2.5.6 3.6.1.3 0 .7-.2 1z"/></svg></span>000 0000 00000</div>

  <div class="hero" role="img" aria-label="Photo of two people holding hands in support"></div>
  <p class="hero-text">Lorem Ipsum Dolor Sit Amet, Consectetur Adipiscing Elit, Sed Do Eiusmod Tempor Incididunt Ut Labore Et Dolore Magna Aliqua. Ut Enim Ad Minim Veniam, Quis Nostrud Exercitation Ullamco Laboris Nisi Ut Aliquip Ex Ea Commodo Consequat. Duis Aute Irure Dolor In Reprehenderit In Voluptate Velit Esse Cillum Dolore Eu Fugiat Nulla Pariatur. Excepteur Sint Occaecat Cupidatat Non Proident, Sunt In Culpa Qui Officia Deserunt Mollit Anim Id Est Laborum.</p>
  <div class="phone-pill hero-phone"><span class="ico"><svg width="30" height="30" viewBox="0 0 24 24"><path fill="#111" d="M6.6 10.8c1.4 2.8 3.8 5.1 6.6 6.6l2.2-2.2c.3-.3.7-.4 1-.2 1.1.4 2.3.6 3.6.6.6 0 1 .4 1 1V20c0 .6-.4 1-1 1C10.6 21 3 13.4 3 4c0-.6.4-1 1-1h3.5c.6 0 1 .4 1 1 0 1.3.2 2.5.6 3.6.1.3 0 .7-.2 1z"/></svg></span>000 0000 00000</div>

  <aside class="sidebar">
    <div class="cat" style="top:0"><svg class="cat-ico" viewBox="0 0 44 44" role="img" aria-label="Medical cross icon"><circle cx="22" cy="22" r="16" fill="#fff"/><path d="M19 12h6v7h7v6h-7v7h-6v-7h-7v-6h7z" fill="#9fb9d3"/></svg><span class="cat-name">Emergency Mental Help</span></div>
    <div class="cat" style="top:62px"><svg class="cat-ico" viewBox="0 0 44 44" role="img" aria-label="Alert icon"><path d="M22 6 40 38H4z" fill="#fff"/><path d="M20 16h4v12h-4zM20 31h4v4h-4z" fill="#8aa8c6"/></svg><span class="cat-name">Suicide</span></div>
    <div class="cat" style="top:124px"><svg class="cat-ico" viewBox="0 0 44 44" role="img" aria-label="Protective shield icon"><path d="M22 5 37 10v11c0 9-6 15-15 18C13 36 7 30 7 21V10z" fill="#fff"/></svg><span class="cat-name">Sexual Assault/Violence<br>Victims</span></div>
    <div class="cat" style="top:186px"><svg class="cat-ico" viewBox="0 0 44 44" role="img" aria-label="Stop sign icon"><path d="M15 5h14l10 10v14L29 39H15L5 29V15z" fill="#fff"/><rect x="12" y="20" width="20" height="4" fill="#7d9cbc"/></svg><span class="cat-name">Sexual Assault/Violence<br>Assaulters</span></div>
    <div class="cat" style="top:248px"><svg class="cat-ico" viewBox="0 0 44 44" role="img" aria-label="Lightning icon"><path d="M25 4 10 25h10l-3 15 17-23H24z" fill="#fff"/></svg><span class="cat-name">Post Trauma</span></div>
    <div class="cat" style="top:310px"><svg class="cat-ico" viewBox="0 0 44 44" role="img" aria-label="Rain cloud icon"><path d="M12 26a7 7 0 0 1 1-14 9 9 0 0 1 17 2 6 6 0 0 1 2 12z" fill="#fff"/><path d="M14 30l-2 6M22 30l-2 6M30 30l-2 6" stroke="#fff" stroke-width="3" stroke-linecap="round"/></svg><span class="cat-name">Depression</span></div>
    <div class="cat" style="top:372px"><svg class="cat-ico" viewBox="0 0 44 44" role="img" aria-label="Pulse icon"><path d="M4 24h9l4-11 6 20 5-13 3 4h9" fill="none" stroke="#fff" stroke-width="4" stroke-linejoin="round" stroke-linecap="round"/></svg><span class="cat-name">Anxiety</span></div>
    <div class="cat" style="top:434px"><svg class="cat-ico" viewBox="0 0 44 44" role="img" aria-label="Bottle and pill icon"><path d="M15 5h6v8l4 5v21H11V18l4-5z" fill="#fff"/><rect x="26" y="27" width="14" height="7" rx="3.5" transform="rotate(-40 33 30)" fill="#fff"/></svg><span class="cat-name">Addictions</span></div>
    <div class="cat" style="top:496px"><svg class="cat-ico" viewBox="0 0 44 44" role="img" aria-label="Bed icon"><path d="M4 12h4v14h32v10h-4v-4H8v4H4z" fill="#fff"/><circle cx="13" cy="21" r="3.5" fill="#fff"/><rect x="19" y="18" width="20" height="7" rx="2" fill="#fff"/></svg><span class="cat-name">Sleep Disorders</span></div>
    <div class="cat" style="top:558px"><svg class="cat-ico" viewBox="0 0 44 44" role="img" aria-label="Plate with cross icon"><path d="M6 28h28a14 7 0 0 1-28 0z" fill="#fff"/><rect x="4" y="33" width="32" height="3" rx="1.5" fill="#fff"/><path d="M30 6l8 8M38 6l-8 8" stroke="#fff" stroke-width="3.5" stroke-linecap="round"/></svg><span class="cat-name">Eating Disorders</span></div>
    <div class="cat" style="top:620px"><svg class="cat-ico" viewBox="0 0 44 44" role="img" aria-label="Falling chart icon"><path d="M8 20h7v18H8zM17 26h7v12h-7zM26 31h7v7h-7z" fill="#fff"/><text x="10" y="16" font-family="Roboto,sans-serif" font-size="15" font-weight="700" fill="#fff">$</text></svg><span class="cat-name">Financial Problems</span></div>
    <div class="cat" style="top:682px"><svg class="cat-ico" viewBox="0 0 44 44" role="img" aria-label="House icon"><path d="M22 6 40 21h-5v17H9V21H4z" fill="#fff"/><rect x="18" y="27" width="8" height="11" fill="#8fa9c4"/></svg><span class="cat-name">Parenthood</span></div>
    <div class="cat" style="top:744px"><svg class="cat-ico" viewBox="0 0 44 44" role="img" aria-label="Two hearts icon"><path d="M14 38 4 28a6 6 0 0 1 10-7 6 6 0 0 1 10 7z" fill="#fff"/><path d="M30 24l-7-7a4.5 4.5 0 0 1 7-5 4.5 4.5 0 0 1 7 5z" fill="#fff"/></svg><span class="cat-name">Relationship</span></div>
  </aside>

  <article class="card" style="left:387px">
    <div class="card-img" role="img" aria-label="Photo of a helpline operator with headset" style="background:radial-gradient(ellipse 50% 45% at 70% 30%,#d8b9a6,rgba(216,185,166,0)),linear-gradient(135deg,#7d6f68,#b8a69b 45%,#5b5552 75%,#3c3a3a)"></div>
    <div class="card-body"><h3 class="card-title">Emergency<br>Mental Help</h3><p class="card-text">Lorem Ipsum Dolor Sit</p></div>
  </article>
  <article class="card" style="left:617px">
    <div class="card-img" role="img" aria-label="Chat app image on green background" style="background:radial-gradient(circle at 50% 50%,#3ec24d 0%,#2a9a38 30%,#1e5e2a 65%,#133b1c)"></div>
    <div class="card-body"><h3 class="card-title">Smart<br>ChatLine</h3><p class="card-text">Lorem Ipsum Dolor Sit</p></div>
  </article>
  <article class="card" style="left:847px">
    <div class="card-img" role="img" aria-label="Photo of a therapy session" style="background:radial-gradient(ellipse 30% 50% at 72% 60%,#8fb1d2,rgba(143,177,210,0)),linear-gradient(180deg,#a8998a 0%,#6f665e 30%,#2c3038 60%,#4a5668)"></div>
    <div class="card-body" style="padding-top:27px"><h3 class="card-title">Therapists</h3><p class="card-text">Lorem Ipsum Dolor Sit<br>Amet, Consectetur</p></div>
  </article>
</div>
</body>
</html>
```